The Verdant Ledger App - Modernization & Graphics User Interface Friendliness Updates

We are Verdant Ledger, and we want to bring a new branding look and graphical user interface to the Verdant Ledger App. The app is a quick reference encyclopedia for all things produce. Boasting articles on over 2,000 produce items, with information ranging from taste and application to geographical and cultural significance. Included in its features are over 10 thousand recipes, and the Verdant Ledger App Harvest Circle – a global initiative to connect farmer, customer, and chef in one sustainable and easy to use application. The design needs to bring a greater sense of social connection – encouraging the user to participate in the 'Harvest Circled' experience voluntarily. The design should reflect a sense of authority reflecting the authenticity and reliability of the provided information, it's writing, and its sources. Download the App here: vledgr.example/install

Target Market(s)

Women and Men between ages 21-55.

Industry/Entity Type

Education

Font styles to use
Serif
Sans Serif

Colors

Designer to choose colors to be used in the design.

Requirements
Must have
• An updated user interface, the intuitive usability of the app is currently non-existent. We are looking to reflect as the authority on produce. The app design must reflect a professional, user-friendly, up-to-date, and trustworthy feel.
Nice to have
• To incorporate the social draw of the Harvest Circle we would like to include on the home page "Social Bubbles" (think Pictoloop stories) which updates with shared photos of produce and their location.
Should not have
• An overly complicated theme, distracting or unprofessional colors, and images.

```html
<!DOCTYPE html>
<html lang="en">
<head>
<meta charset="utf-8">
<title>Verdant Ledger – Home</title>
<link rel="stylesheet" href="https://fonts.googleapis.com/css2?family=Roboto:wght@400;500&display=swap">
<style>
:root{
  --bg:#3a3a3a;
  --screen:#f7f7f7;
  --green:#189a1a;
  --ink:#111;
  --muted:#555;
  --band:#c9c9c9;
  --filter:#dcdcdc;
  --badge:#f0344f;
  --nav-muted:#6a6a6a;
}
*{box-sizing:border-box;margin:0;padding:0}
html,body{width:1200px;height:857px;overflow:hidden;background:var(--bg);font-family:"Roboto",Arial,sans-serif;color:var(--ink)}
.screen{position:absolute;left:368px;top:19px;width:403px;height:711px;background:var(--screen);transform:scale(1.15);transform-origin:0 0;overflow:hidden;border:2px solid #111}
.status{height:22px;display:flex;align-items:center;justify-content:space-between;padding:0 8px;font-size:10px}
.status .dots{letter-spacing:-1px;font-size:9px}
.status .battery{display:flex;align-items:center;gap:4px}
.status .cell{width:20px;height:9px;border:1px solid #111;border-radius:2px;padding:1px}
.status .cell span{display:block;width:85%;height:100%;background:#111}
.header{height:48px;display:flex;align-items:center;justify-content:space-between;padding:0 16px 0 12px}
.brand{font-family:"Roboto",Arial,sans-serif;font-weight:500;color:var(--green);font-size:22px;letter-spacing:0}
.fav{position:relative;width:36px;height:28px}
.fav b{position:absolute;left:16px;top:5px;background:var(--green);color:#fff;font-size:10px;font-weight:500;border-radius:8px;padding:0 3px;line-height:13px}
.searchbar{height:47px;background:var(--band);display:flex;align-items:center;padding-left:7px}
.search{width:319px;height:32px;background:#fff;border-radius:3px;display:flex;align-items:center;justify-content:center;gap:6px;color:var(--muted);font-size:13px}
.filter{margin-left:auto;width:66px;height:47px;background:var(--filter);display:flex;flex-direction:column;align-items:center;justify-content:center;font-size:9px;gap:4px}
.filter i{display:block;width:36px;height:1px;background:#fff;box-shadow:0 -6px 0 #fff,0 6px 0 #fff,0 -12px 0 #fff;margin-top:10px}
.section{height:31px;display:flex;align-items:flex-end;padding:0 0 4px 13px;font-size:10.5px;border-bottom:1px solid var(--green)}
.item{height:126px;display:flex;border-bottom:1px solid var(--green);padding:6px 0 0 10px}
.photo{width:185px;height:112px;border-radius:30px}
.papaya{background:radial-gradient(ellipse at 50% 55%,#f07a25 0 30%,#9bb23a 55%,transparent 70%)}
.fava{background:radial-gradient(ellipse at 50% 50%,#6fb03a 0 40%,#bcd77d 58%,transparent 70%)}
.kiwi{background:radial-gradient(ellipse at 50% 50%,#a28a4a 0 40%,#7fb33a 55%,transparent 70%)}
.rambutan{background:radial-gradient(ellipse at 50% 50%,#8a1f2a 0 40%,#c45a5a 55%,transparent 70%)}
.body{margin-left:18px;width:145px;position:relative}
.body h2{font-size:13.5px;font-weight:500;letter-spacing:.3px;margin-top:-1px}
.body p{font-size:8.6px;line-height:10.5px;margin-top:4px}
.meta{position:absolute;left:0;top:88px;width:160px;display:flex;align-items:center;font-size:10px;color:var(--muted)}
.meta .acts{margin-left:auto;display:flex;gap:20px;align-items:center}
.nav{position:absolute;left:0;right:0;bottom:0;height:57px;border-top:1px solid var(--green);display:flex;justify-content:space-around;align-items:flex-end;padding:0 4px 4px}
.tab{position:relative;display:flex;flex-direction:column;align-items:center;gap:3px;font-size:9.5px;color:var(--nav-muted);width:70px}
.tab.active{color:var(--green)}
.tab .count{position:absolute;top:-3px;left:42px;background:var(--badge);color:#fff;font-size:9.5px;border-radius:7px;padding:0 4px;line-height:13px}
</style>
</head>
<body>
<main class="screen">
  <div class="status">
    <span class="dots">●●●●● <svg width="10" height="8" viewBox="0 0 10 8"><path d="M1 3a6 6 0 0 1 8 0M2.5 4.6a4 4 0 0 1 5 0M5 7.5l1.2-1.3a2 2 0 0 0-2.4 0z" fill="none" stroke="#111" stroke-width="1.2"/></svg></span>
    <span>11:47</span>
    <span class="battery">86% <span class="cell"><span></span></span></span>
  </div>
  <header class="header">
    <div class="fav"><svg width="28" height="26" viewBox="0 0 28 26"><path d="M14 23C4 15 2 11 2 8a6 6 0 0 1 12-1 6 6 0 0 1 12 1c0 3-2 7-12 15z" fill="none" stroke="#189a1a" stroke-width="1.6"/></svg><b>20</b></div>
    <h1 class="brand">Verdant Ledger</h1>
    <svg width="28" height="28" viewBox="0 0 28 28"><g fill="none" stroke="#189a1a" stroke-width="1.4"><circle cx="14" cy="14" r="5"/><path d="M12 2h4l.7 3.4 2.8 1.2 2.9-2 2.8 2.9-2 2.9 1.2 2.8L26 12v4l-3.4.7-1.2 2.8 2 2.9-2.9 2.8-2.9-2-2.8 1.2L16 26h-4l-.7-3.4-2.8-1.2-2.9 2-2.8-2.9 2-2.9-1.2-2.8L2 16v-4l3.4-.7 1.2-2.8-2-2.9 2.9-2.8 2.9 2 2.8-1.2z"/></g></svg>
  </header>
  <div class="searchbar">
    <div class="search"><svg width="14" height="14" viewBox="0 0 14 14"><circle cx="5.5" cy="5.5" r="4.5" fill="none" stroke="#555" stroke-width="1.4"/><path d="M9 9l4 4" stroke="#555" stroke-width="1.4"/></svg>Search</div>
    <div class="filter"><i></i>Filter</div>
  </div>
  <div class="section">RECENT UPDATES</div>

  <article class="item">
    <div class="photo papaya" role="img" aria-label="Photo of whole and halved papaya"></div>
    <div class="body"><h2>Lorem Ipsum</h2><p>Lorem ipsum dolor sit amet, con-sectetuer adipiscing elit, sed diam nonummy nibh euismod tincidunt ut laoreet dolore magna aliquam erat volutpat. Ut wisi</p>
      <div class="meta">Today<span class="acts"><svg width="26" height="22" viewBox="0 0 26 22"><path d="M13 20C4 13 2 10 2 7a5.5 5.5 0 0 1 11-1 5.5 5.5 0 0 1 11 1c0 3-2 6-11 13z" fill="none" stroke="#189a1a" stroke-width="1.5"/></svg><svg width="22" height="22" viewBox="0 0 22 22"><g fill="#189a1a"><circle cx="17" cy="4" r="3"/><circle cx="5" cy="11" r="3"/><circle cx="17" cy="18" r="3"/></g><path d="M17 4L5 11l12 7" fill="none" stroke="#189a1a" stroke-width="1.6"/></svg></span></div></div>
  </article>
  <article class="item">
    <div class="photo fava" role="img" aria-label="Photo of fava bean pods and shelled beans"></div>
    <div class="body"><h2>Lorem Ipsum</h2><p>Lorem ipsum dolor sit amet, con-sectetuer adipiscing elit, sed diam nonummy nibh euismod tincidunt ut laoreet dolore magna aliquam erat volutpat. Ut wisi</p>
      <div class="meta">Today<span class="acts"><svg width="26" height="22" viewBox="0 0 26 22"><path d="M13 20C4 13 2 10 2 7a5.5 5.5 0 0 1 11-1 5.5 5.5 0 0 1 11 1c0 3-2 6-11 13z" fill="#189a1a" stroke="#189a1a" stroke-width="1.5"/></svg><svg width="22" height="22" viewBox="0 0 22 22"><g fill="#189a1a"><circle cx="17" cy="4" r="3"/><circle cx="5" cy="11" r="3"/><circle cx="17" cy="18" r="3"/></g><path d="M17 4L5 11l12 7" fill="none" stroke="#189a1a" stroke-width="1.6"/></svg></span></div></div>
  </article>
  <article class="item">
    <div class="photo kiwi" role="img" aria-label="Photo of whole and halved kiwifruit"></div>
    <div class="body"><h2>Lorem Ipsum</h2><p>Lorem ipsum dolor sit amet, con-sectetuer adipiscing elit, sed diam nonummy nibh euismod tincidunt ut laoreet dolore magna aliquam erat volutpat. Ut wisi</p>
      <div class="meta">Yesterday<span class="acts"><svg width="26" height="22" viewBox="0 0 26 22"><path d="M13 20C4 13 2 10 2 7a5.5 5.5 0 0 1 11-1 5.5 5.5 0 0 1 11 1c0 3-2 6-11 13z" fill="none" stroke="#189a1a" stroke-width="1.5"/></svg><svg width="22" height="22" viewBox="0 0 22 22"><g fill="#189a1a"><circle cx="17" cy="4" r="3"/><circle cx="5" cy="11" r="3"/><circle cx="17" cy="18" r="3"/></g><path d="M17 4L5 11l12 7" fill="none" stroke="#189a1a" stroke-width="1.6"/></svg></span></div></div>
  </article>
  <article class="item">
    <div class="photo rambutan" role="img" aria-label="Photo of a pile of rambutans"></div>
    <div class="body"><h2>Lorem Ipsum</h2><p>Lorem ipsum dolor sit amet, con-sectetuer adipiscing elit, sed diam nonummy nibh euismod tincidunt ut laoreet dolore magna aliquam erat volutpat. Ut wisi</p>
      <div class="meta">Yesterday<span class="acts"><svg width="26" height="22" viewBox="0 0 26 22"><path d="M13 20C4 13 2 10 2 7a5.5 5.5 0 0 1 11-1 5.5 5.5 0 0 1 11 1c0 3-2 6-11 13z" fill="none" stroke="#189a1a" stroke-width="1.5"/></svg><svg width="22" height="22" viewBox="0 0 22 22"><g fill="#189a1a"><circle cx="17" cy="4" r="3"/><circle cx="5" cy="11" r="3"/><circle cx="17" cy="18" r="3"/></g><path d="M17 4L5 11l12 7" fill="none" stroke="#189a1a" stroke-width="1.6"/></svg></span></div></div>
  </article>

  <nav class="nav">
    <a class="tab active"><svg width="30" height="28" viewBox="0 0 30 28"><path d="M15 2L2 14h4v12h7v-8h4v8h7V14h4z" fill="#189a1a"/></svg>Home</a>
    <a class="tab"><svg width="28" height="28" viewBox="0 0 28 28"><g fill="#6a6a6a"><rect x="2" y="2" width="6" height="6"/><rect x="11" y="2" width="6" height="6"/><rect x="20" y="2" width="6" height="6"/><rect x="2" y="11" width="6" height="6"/><rect x="11" y="11" width="6" height="6"/><rect x="20" y="11" width="6" height="6"/><rect x="2" y="20" width="6" height="6"/><rect x="11" y="20" width="6" height="6"/><rect x="20" y="20" width="6" height="6"/></g></svg>Category</a>
    <a class="tab"><svg width="30" height="28" viewBox="0 0 30 28"><g fill="none" stroke="#6a6a6a" stroke-width="1.4"><circle cx="15" cy="16" r="10"/><path d="M15 10v6l4 3M5 4l3 3M8 2v4"/></g></svg>Updated<span class="count">14</span></a>
    <a class="tab"><svg width="24" height="28" viewBox="0 0 24 28"><path d="M12 27S3 16 3 10a9 9 0 0 1 18 0c0 6-9 17-9 17z" fill="none" stroke="#6a6a6a" stroke-width="1.4"/><circle cx="12" cy="10" r="3.5" fill="#6a6a6a"/></svg>Spotted<span class="count">21</span></a>
    <a class="tab"><svg width="32" height="28" viewBox="0 0 32 28"><g fill="none" stroke="#6a6a6a" stroke-width="1.4"><path d="M4 13h24c0 7-5 11-12 11S4 20 4 13zM10 26h12M7 4h14v9M10 7h8M10 10h8M22 12l7-10"/></g></svg>Recipes</a>
  </nav>
</main>
</body>
</html>
```